依頼詳細
・新生活をスタートするような大学生が主なターゲットになります。
・家電と人の写真を入れてください。
・カラーはサイトに合わせなくても新生活感が出る方でお願いいたします。
・まずは、300×250ピクセルのサイズで提出お願いいたします。
記載項目
タイトル:新生活スタートするならレンタルがおすすめ!! キャッチ:①学生様限定プラン!! ②最大40%OFF!! ③家電3点セット月々1,194円!!
サイズ
• 300 x 250 ( ミディアムレクタングル )
• 250 x 250 ( スクエアポップアップ )
• 200 x 200 ( スクエア )
• 600×500,640×200,320×50,320×100,1200×628
希望イメージ
シンプル 複雑
単色 カラフル
暗い 明るい
日常 高級
遊び心 厳粛
未来的 伝統的
女性的 男性的
希望する色
赤系、水色系、黄・オレンジ系
納品ファイル
• 高解像度JPG (.jpg)
• イラストレーター形式 (.ai)
• PNG形式 (.png)

新生活をスタートする雰囲気のあるデザインが気に入りました。

この度はご提案頂きありがとうございました。
今後ともよろしくお願いいたします。

```html
<!DOCTYPE html>
<html lang="ja">
<head>
<meta charset="UTF-8">
<title>新生活レンタル 学生様限定プラン</title>
<link href="https://fonts.googleapis.com/css2?family=M+PLUS+Rounded+1c:wght@800;900&family=Noto+Serif+JP:wght@900&display=swap" rel="stylesheet">
<style>
  :root{
    --sky-top:#8cc6ee;
    --sky-bottom:#d9eefb;
    --pink:#e8457e;
    --pink-deep:#d62f6c;
    --yellow:#fff200;
    --yellow-soft:#f4ee3a;
    --navy:#1d3f8f;
    --ink:#1a1a1a;
    --white:#ffffff;
    --blossom:#f3e4ea;
    --appliance:#d7dadd;
    --shirt-white:#f4f1ec;
    --shirt-yellow:#f3ea7a;
    --shirt-blue:#cfe0f2;
    --hair:#5a3a28;
    --skin:#f0cdb4;
  }
  *{margin:0;padding:0;box-sizing:border-box;}
  html,body{width:1200px;height:1000px;overflow:hidden;}
  body{font-family:"M PLUS Rounded 1c",sans-serif;}
  .banner{
    position:relative;width:1200px;height:1000px;overflow:hidden;
    background:linear-gradient(180deg,var(--sky-top) 0%,var(--sky-bottom) 70%);
  }
  .photo{position:absolute;}
  .photo-blossoms{
    right:0;top:250px;width:520px;height:750px;
    background:radial-gradient(ellipse at 65% 55%,#fbf1f4 0%,var(--blossom) 40%,rgba(226,206,214,.85) 65%,rgba(243,228,234,0) 90%);
  }
  .photo-appliances{
    left:0;top:0;width:300px;height:350px;
    background:linear-gradient(160deg,#eef0f2 0%,var(--appliance) 55%,#7d8288 100%);
    border-bottom-right-radius:20px;
  }
  .photo-people{
    left:0;top:580px;width:1200px;height:420px;
    background:
      linear-gradient(180deg,var(--hair) 0%,var(--hair) 14%,var(--skin) 26%,var(--skin) 44%,rgba(240,205,180,0) 58%),
      linear-gradient(90deg,var(--shirt-white) 0%,var(--shirt-white) 24%,var(--shirt-yellow) 30%,var(--shirt-yellow) 44%,var(--shirt-white) 50%,var(--shirt-white) 64%,var(--shirt-blue) 70%,var(--shirt-blue) 100%);
    -webkit-mask:linear-gradient(180deg,rgba(0,0,0,0) 0%,#000 8%);
    mask:linear-gradient(180deg,rgba(0,0,0,0) 0%,#000 8%);
  }
  .outline-white{
    text-shadow:4px 0 var(--white),-4px 0 var(--white),0 4px var(--white),0 -4px var(--white),3px 3px var(--white),-3px -3px var(--white),3px -3px var(--white),-3px 3px var(--white);
  }
  .headline-line1{
    position:absolute;left:292px;top:26px;
    color:var(--pink);font-weight:900;white-space:nowrap;
    font-size:92px;line-height:104px;letter-spacing:-3px;
  }
  .headline-line1 .small{font-size:66px;letter-spacing:-2px;}
  .headline-line2{position:absolute;left:258px;top:132px;display:flex;align-items:center;white-space:nowrap;}
  .rental-tag{
    background:var(--pink);color:var(--white);font-weight:900;
    font-size:92px;line-height:1;padding:4px 16px 12px;border-radius:30px;
    border:5px solid var(--white);letter-spacing:-3px;
  }
  .recommend{
    color:var(--pink);font-weight:900;font-size:76px;margin-left:8px;letter-spacing:-2px;
  }
  .student-plan{
    position:absolute;left:334px;top:264px;
    color:var(--yellow-soft);font-weight:900;font-size:54px;letter-spacing:-2px;white-space:nowrap;
    text-shadow:3px 0 #3a6a4a,-3px 0 #3a6a4a,0 3px #3a6a4a,0 -3px #3a6a4a,2px 2px #3a6a4a,-2px -2px #3a6a4a,2px -2px #3a6a4a,-2px 2px #3a6a4a;
  }
  .max-pill{
    position:absolute;left:360px;top:342px;width:396px;height:72px;
    background:var(--ink);color:var(--white);border-radius:36px;border:3px solid var(--white);
    font-weight:900;font-size:42px;display:flex;align-items:center;justify-content:center;gap:20px;
  }
  .discount{
    position:absolute;left:20px;top:340px;white-space:nowrap;
    font-family:"Noto Serif JP",serif;font-weight:900;color:var(--yellow);
    text-shadow:5px 0 var(--navy),-5px 0 var(--navy),0 5px var(--navy),0 -5px var(--navy),4px 4px var(--navy),-4px -4px var(--navy),4px -4px var(--navy),-4px 4px var(--navy),8px 8px 6px rgba(0,0,0,.35);
  }
  .discount-num{font-size:300px;line-height:260px;letter-spacing:-12px;}
  .discount-unit{font-size:136px;letter-spacing:-6px;}
  .price-card{
    position:absolute;left:768px;top:258px;width:414px;height:342px;
    background:rgba(255,255,255,.95);
  }
  .set-label{
    position:absolute;right:24px;top:8px;text-align:right;
    font-weight:900;font-size:60px;line-height:70px;color:var(--ink);letter-spacing:-2px;
  }
  .set-label .num{font-size:74px;}
  .monthly{
    position:absolute;left:30px;top:108px;width:76px;height:76px;border-radius:50%;
    background:var(--ink);color:var(--white);font-weight:900;font-size:32px;
    display:flex;align-items:center;justify-content:center;
  }
  .price{
    position:absolute;left:12px;top:170px;white-space:nowrap;
    font-family:"Noto Serif JP",serif;font-weight:900;color:var(--pink-deep);
  }
  .price-num{font-size:124px;letter-spacing:-6px;}
  .price-yen{font-family:"M PLUS Rounded 1c",sans-serif;font-size:52px;}
</style>
</head>
<body>
<div class="banner">
  <div class="photo photo-blossoms" role="img" aria-label="満開の桜の写真"></div>
  <div class="photo photo-appliances" role="img" aria-label="洗濯機・冷蔵庫・電子レンジの家電写真"></div>
  <div class="photo photo-people" role="img" aria-label="人差し指を立てて笑顔を見せる学生4人の写真"></div>

  <div class="headline-line1 outline-white">新生活スタート<span class="small">するなら</span></div>
  <div class="headline-line2">
    <span class="rental-tag">レンタル</span><span class="recommend outline-white">がおすすめ!!</span>
  </div>

  <div class="student-plan">学生様限定プラン!!</div>
  <div class="discount"><span class="discount-num">40</span><span class="discount-unit">%OFF</span></div>
  <div class="max-pill"><span>最大</span><span>なんと!</span></div>

  <div class="price-card">
    <div class="set-label">家電<span class="num">3</span>点<br>セット</div>
    <div class="monthly">月々</div>
    <div class="price"><span class="price-num">1,194</span><span class="price-yen">円</span></div>
  </div>
</div>
</body>
</html>
```